Banner 34"x81"

This is for a Pull Up Banner
I am supplying a sample of my logo and some of my art work for you to incorporate into an upright banner.
Please business name:LuellaRo OpenHarbor Psychotherapy
phone number: 583-214-9067 NOT THE ONE ON THE BUSINESS CARD

```html
<!DOCTYPE html>
<html lang="en">
<head>
<meta charset="utf-8">
<title>LuellaRo OpenHarbor Psychotherapy – Pull Up Banner</title>
<link rel="stylesheet" href="https://fonts.googleapis.com/css2?family=Bebas+Neue&family=Open+Sans:wght@400;600&display=swap">
<style>
  :root {
    --page-bg: #e6e6e6;
    --banner-blue: #1f3a8f;
    --accent-gold: #cdb76f;
    --band-gold-light: #c9a64a;
    --band-gold-dark: #9c7a24;
    --text-white: #ffffff;
    --photo-blue: #2a5fd0;
    --photo-dark: #1b1b24;
  }
  * { margin: 0; padding: 0; box-sizing: border-box; }
  html, body {
    width: 1200px; height: 800px; overflow: hidden;
    background: var(--page-bg);
  }
  .banner {
    position: absolute; left: 440px; top: 19px;
    width: 320px; height: 762px;
    background: var(--banner-blue);
    overflow: hidden;
    box-shadow: 0 6px 24px rgba(0,0,0,0.18);
  }
  .banner__shapes { position: absolute; inset: 0; }
  .brand-mark {
    position: absolute; left: 0; right: 0; top: 108px;
    display: flex; align-items: center; justify-content: center; gap: 10px;
    font-family: "Bebas Neue", sans-serif; font-size: 46px; line-height: 1;
    color: var(--text-white);
  }
  .brand-mark__square {
    width: 18px; height: 18px; background: var(--accent-gold);
  }
  .business-name {
    position: absolute; left: 0; right: 0; top: 205px;
    text-align: center;
    font-family: "Bebas Neue", sans-serif; font-weight: 400;
    font-size: 47px; line-height: 49px; letter-spacing: 0.3px;
    color: var(--text-white);
  }
  .portrait {
    position: absolute; left: 82px; top: 352px;
    width: 178px; height: 290px;
    border-radius: 70px 70px 0 0;
    background: linear-gradient(180deg, var(--photo-dark) 0%, #3a3340 28%, var(--photo-blue) 52%, #2450b8 78%, #6d6f78 100%);
  }
  .contact-band {
    position: absolute; left: 0; right: 0; bottom: 0; height: 130px;
    background: linear-gradient(160deg, var(--band-gold-light) 0%, #b58f32 50%, var(--band-gold-dark) 100%);
    color: var(--text-white); text-align: center;
  }
  .contact-band__phone {
    margin-top: 18px;
    font-family: "Bebas Neue", sans-serif; font-size: 46px; line-height: 1;
    letter-spacing: 0.5px;
  }
  .contact-band__email {
    margin-top: 6px;
    font-family: "Open Sans", sans-serif; font-size: 13px;
  }
  .contact-band__social {
    margin-top: 6px;
    display: flex; justify-content: center; gap: 14px;
    font-family: "Open Sans", sans-serif; font-size: 11.5px;
  }
  .social-handle { display: flex; align-items: center; gap: 4px; }
  .social-handle__dot {
    width: 10px; height: 10px; border-radius: 50%;
    background: var(--text-white);
  }
</style>
</head>
<body>
  <main class="banner">
    <svg class="banner__shapes" viewBox="0 0 320 762" width="320" height="762" aria-hidden="true">
      <path d="M176 0 H320 V118 C305 108 296 96 284 82 C270 70 262 62 248 58 C232 56 220 50 206 44 C192 40 182 30 176 20 Z" fill="var(--accent-gold)"/>
      <polygon points="0,387 160,482 160,537 0,442" fill="var(--accent-gold)"/>
      <polygon points="320,387 160,482 160,537 320,442" fill="var(--accent-gold)"/>
    </svg>

    <div class="brand-mark">
      <span class="brand-mark__square"></span>
      <span class="brand-mark__name">LuellaRo</span>
    </div>

    <h1 class="business-name">LuellaRo<br>OpenHarbor<br>Psychotherapy</h1>

    <div class="portrait" role="img" aria-label="Portrait photo of the therapist, seated, wearing a blue top"></div>

    <footer class="contact-band">
      <p class="contact-band__phone">583-214-9067</p>
      <p class="contact-band__email">LuellaOpenHarbor@mail.com</p>
      <div class="contact-band__social">
        <span class="social-handle"><span class="social-handle__dot"></span>@LuellaOpenHarbor</span>
        <span class="social-handle"><span class="social-handle__dot"></span>@LuellaHarbor</span>
      </div>
    </footer>
  </main>
</body>
</html>
```